HIGH END MEDICAL/ANTI-AGING START-UP BROCHURE + BUSINESS CARDS

Fernridgewellnessco.example needs a brochure which details our two top selling products. The Vital Matrix Profile Review (VMP) coupled with the 4(16) Plan.

Here is some information about the VMP and the 4(16) plan. Please see our website for pictures and color.

VMP-Vital Matrix Profile and Fernridge
Fernridge Wellness Co is changing the way people look at health by bringing the focus back to the physical examination and patient centered care. It's our new, cutting edge system, Vital Matrix Profile, that allows us to have unparalleled patient outcomes. Vital Matrix Profile is a true deep dive into the individual. The protocol assesses, measures and tracking over 70 different bio-parameters such as hormone balance, tissue health, muscle mass, fat mass, frame mass, water content, water distribution, and acid/alkaline balance. This new analytics tool allows hyper individualized and customized weight loss and health programs to evolve in a new and never before seen way.

The 4(16) Plan
The 4(16) Cleanse plan works by creating a full metabolic reset geared towards facilitation of hormone optimization and balance as well as toxicity and fat removal. Toxins are fat soluble and often need targeted nutritional strategy for long-term weight loss to occur; this is why many people do not lose weight even on calorie restricted diets with exercise plans until they use proper nutritional protocol. The 4(16) Cleanse allows for fat cells to be released and disposed of while at the same time adding deficient nutrients back into the tissues, helping you to not only lose weight, but reach optimal health and hormonal balance at the same time.

Target Market(s)

High-end and upscale clients looking for boutique medical services. We deal with clients mostly in executive level finance.

Industry/Entity Type

Medical

Contact Information for Business Card

-Must have our logo
-website (fernridgewellnessco.example)
-a space for our titles, "Dr. Anton Pelsing, Founder" & "Rosalind Pelsing, Program Director"
-office phone number and our cell phone numbers (we will give you our cell phone numbers later)

Font styles to use
Serif
Sans Serif

Colors
0355a3
0493ce
00a990
ffffff
000000
919191
474747

Requirements
Must have
• Brochure and business cards must be VERY modern, creative and sophisticated.
Nice to have
• Usage of the company colors and logo in a new and interesting way.
Should not have
• Do not use colors outside of our logo + black + grey or white.
• Nothing cartoonish.

```html
<!DOCTYPE html>
<html lang="en">
<head>
<meta charset="utf-8">
<title>Fernridge Wellness Co — Trifold Brochure</title>
<link href="https://fonts.googleapis.com/css2?family=Montserrat:wght@400;700;800&family=Open+Sans:ital,wght@0,400;0,600;0,700;1,400&display=swap" rel="stylesheet">
<style>
:root{
  --bg:#e4e4e4;
  --green:#1c9a3b;
  --green-dark:#147a2d;
  --blue:#3a62d6;
  --blue-deep:#2c4fc0;
  --white:#ffffff;
  --ink:#474747;
  --grey:#919191;
}
*{box-sizing:border-box;margin:0;padding:0}
html,body{width:800px;height:1200px;overflow:hidden;background:var(--bg)}
body{position:relative;font-family:"Open Sans",Arial,sans-serif;color:var(--ink)}
.spread{position:absolute;left:40px;width:720px;height:557px;background:var(--white);overflow:hidden;box-shadow:0 4px 14px rgba(0,0,0,.15)}
.spread--outside{top:28px}
.spread--inside{top:615px}
.spread__art{position:absolute;inset:0;width:720px;height:557px}
.fold{position:absolute;top:0;bottom:0;width:1px;background:rgba(0,0,0,.06)}
.block{position:absolute}
.lead{color:var(--white);font-weight:700;font-size:10.5px;line-height:1.38}
.heading{font-family:"Montserrat",Arial,sans-serif;font-weight:800;font-size:15px;letter-spacing:.3px}
.heading span{font-weight:400}
.subheading{font-family:"Montserrat",Arial,sans-serif;font-size:12px;font-weight:400}
.body{font-size:7.3px;line-height:1.45;text-align:justify}
.body + .body{margin-top:8px}
.on-dark{color:var(--white)}
.rule{height:1px;background:rgba(255,255,255,.55);margin:6px 0}
.rule--green{background:var(--green)}
.contact{color:var(--white);font-size:9.5px;line-height:1.35}
.contact li{list-style:none;display:flex;gap:8px;margin-bottom:6px}
.contact svg{flex:0 0 10px;margin-top:2px}
.brand{display:flex;flex-direction:column;align-items:center;gap:6px}
.brand__mark{width:34px;height:34px;border-radius:50%;background:var(--green)}
.brand__name{font-family:"Open Sans",Arial,sans-serif;font-weight:700;font-size:14px;color:var(--blue);letter-spacing:.5px}
.site{color:var(--white);font-size:9.5px;font-weight:600}
.title-green{color:var(--green);font-family:"Montserrat",Arial,sans-serif;font-weight:800;font-size:13px}
.title-green span{font-weight:400}
.title-white{color:var(--white);font-family:"Montserrat",Arial,sans-serif;font-weight:700;font-size:13px}
.title-white span{font-weight:400}
.tagline{color:var(--green);font-weight:700;font-size:11px;line-height:1.25}
</style>
</head>
<body>

<section class="spread spread--outside" aria-label="Brochure outside">
  <svg class="spread__art" viewBox="0 0 720 557">
    <defs>
      <linearGradient id="portraitTone" x1="0" y1="0" x2="1" y2="1">
        <stop offset="0" stop-color="#9cbd5a"/><stop offset="1" stop-color="#4f7f30"/>
      </linearGradient>
      <linearGradient id="foodTone" x1="0" y1="0" x2="1" y2="1">
        <stop offset="0" stop-color="#d9d6d0"/><stop offset=".5" stop-color="#b78a6a"/><stop offset="1" stop-color="#c9c3bb"/>
      </linearGradient>
      <linearGradient id="mapTone" x1="0" y1="0" x2="1" y2="1">
        <stop offset="0" stop-color="#eef0ea"/><stop offset="1" stop-color="#c9d8e8"/>
      </linearGradient>
    </defs>
    <rect x="0" y="0" width="240" height="230" fill="url(#portraitTone)" role="img" aria-label="Photo of a smiling woman holding a bowl of fresh vegetables"/>
    <path d="M240,0 H720 V60 C600,40 440,30 240,80 Z" fill="#efefef"/>
    <path d="M240,80 C440,30 600,40 720,60 V330 C560,390 420,360 300,300 L240,290 Z" fill="url(#foodTone)" role="img" aria-label="Photo of bowls of fruit, nuts, seeds and beans on a white table"/>
    <path d="M240,0 H720 V120 C620,70 480,60 560,0 Z" fill="#f4f4f4"/>
    <path d="M0,236 C70,201 160,175 240,145 L240,557 L0,557 Z" fill="var(--green)"/>
    <path d="M0,229 C70,194 160,168 240,138" fill="none" stroke="var(--blue)" stroke-width="3"/>
    <path d="M240,290 C360,330 440,395 560,380 C630,372 680,350 720,330 L720,557 L240,557 Z" fill="var(--green)"/>
    <path d="M240,282 C360,322 440,387 560,372 C630,364 680,342 720,322" fill="none" stroke="var(--blue)" stroke-width="6"/>
    <circle cx="325" cy="300" r="55" fill="url(#mapTone)" stroke="var(--blue)" stroke-width="6" role="img" aria-label="Street map showing the office location"/>
  </svg>
  <div class="fold" style="left:240px"></div>
  <div class="fold" style="left:480px"></div>

  <div class="block brand" style="left:500px;top:30px;width:200px">
    <span class="brand__mark"></span>
    <span class="brand__name">Fernridge Wellness Co</span>
  </div>

  <p class="block lead" style="left:18px;top:244px;width:210px">Fernridge Wellness Co was formed to bring empathy, understanding, and real solutions to health care, combating 21st century disease with science and nutrition, all to help people reach their maximum potential.</p>
  <div class="block" style="left:18px;top:350px;width:206px">
    <div class="rule"></div>
    <h2 class="heading on-dark">ABOUT <span>US</span></h2>
    <h3 class="subheading on-dark" style="margin-top:5px">Founders</h3>
    <p class="body on-dark" style="margin-top:4px">Dr. Anton and Rosalind Pelsing met in 2011 in St. Paul Minnesota. Living in the same part of town, the Highland Park area, their paths crossed serendipitously while working out at the gym, studying health subject matter at the local coffee shop and eating healthy bites out on the town with friends! Dr. Anton interrupted Rosalind on the elliptical one day and asked for her phone number...and the rest is history!</p>
    <p class="body on-dark">Their dedication to a healthy lifestyle includes a balanced diet of whole foods, vitamins, quarterly detoxification, regular exercise, sauna and meditation. The Pelsings decompress and de-stress through travel and are avid cross country skiers and winter sport enthusiasts.</p>
  </div>

  <ul class="block contact" style="left:262px;top:400px;width:210px">
    <li><svg width="10" height="12" viewBox="0 0 10 12"><path d="M5 0C2.2 0 0 2.2 0 4.8 0 8.4 5 12 5 12s5-3.6 5-7.2C10 2.2 7.8 0 5 0zm0 6.6A1.8 1.8 0 1 1 5 3a1.8 1.8 0 0 1 0 3.6z" fill="#fff"/></svg><span>Fernridge Wellness Co<br>212 Larch Ave. Suite 40<br>Harborview CT, 06999</span></li>
    <li><svg width="10" height="12" viewBox="0 0 10 12"><path d="M5 0C2.2 0 0 2.2 0 4.8 0 8.4 5 12 5 12s5-3.6 5-7.2C10 2.2 7.8 0 5 0zm0 6.6A1.8 1.8 0 1 1 5 3a1.8 1.8 0 0 1 0 3.6z" fill="#fff"/></svg><span>New York Office:<br>88 Meridian St.<br>Lakeport, NY, 10999</span></li>
    <li><svg width="10" height="8" viewBox="0 0 10 8"><rect x=".5" y=".5" width="9" height="7" fill="none" stroke="#fff"/><path d="M.5 .5 5 4.5 9.5 .5" fill="none" stroke="#fff"/></svg><span>info@fernridgewellnessco.example</span></li>
    <li><svg width="10" height="10" viewBox="0 0 10 10"><path d="M2 0 4 2.5 3 4c.6 1.3 1.7 2.4 3 3l1.5-1L10 8 8.5 10C4 10 0 6 0 1.5z" fill="#fff"/></svg><span>(555) 014-2870</span></li>
    <li><svg width="10" height="10" viewBox="0 0 10 10"><circle cx="5" cy="5" r="4.5" fill="none" stroke="#fff"/><path d="M.5 5h9M5 .5c-2.5 3-2.5 6 0 9M5 .5c2.5 3 2.5 6 0 9" fill="none" stroke="#fff"/></svg><span>www.fernridgewellnessco.example</span></li>
  </ul>

  <p class="block site" style="left:500px;top:520px;width:205px;text-align:right">www.fernridgewellnessco.example</p>
</section>

<section class="spread spread--inside" aria-label="Brochure inside">
  <svg class="spread__art" viewBox="0 0 720 557">
    <defs>
      <linearGradient id="saladTone" x1="0" y1="0" x2="1" y2="1">
        <stop offset="0" stop-color="#7a8a5a"/><stop offset=".6" stop-color="#c3a06a"/><stop offset="1" stop-color="#5f6b4a"/>
      </linearGradient>
      <linearGradient id="bowlTone" x1="0" y1="0" x2="1" y2="1">
        <stop offset="0" stop-color="#c98a4a"/><stop offset="1" stop-color="#5d8a3a"/>
      </linearGradient>
      <linearGradient id="smoothieTone" x1="0" y1="0" x2="1" y2="1">
        <stop offset="0" stop-color="#cfe0a8"/><stop offset="1" stop-color="#6da340"/>
      </linearGradient>
    </defs>
    <path d="M0,0 H240 V120 C170,150 80,165 0,150 Z" fill="url(#saladTone)" role="img" aria-label="Photo of a fresh salad bowl with avocado, carrot and broccoli"/>
    <path d="M0,158 C80,173 170,158 240,128" fill="none" stroke="var(--green)" stroke-width="6"/>
    <path d="M0,166 C80,181 170,166 240,136" fill="none" stroke="var(--blue)" stroke-width="2"/>
    <path d="M240,0 H720 V557 H455 C490,470 485,380 435,335 C375,285 300,300 240,330 Z" fill="var(--blue)"/>
    <path d="M240,338 C300,308 372,295 430,342 C478,385 482,470 447,557" fill="none" stroke="var(--green)" stroke-width="6"/>
    <circle cx="385" cy="255" r="46" fill="url(#bowlTone)" stroke="var(--green)" stroke-width="6" role="img" aria-label="Photo of a healthy bowl with kiwi, berries and nuts"/>
    <circle cx="345" cy="355" r="62" fill="url(#smoothieTone)" stroke="var(--green)" stroke-width="6" role="img" aria-label="Photo of a green smoothie jar with spinach and mint"/>
  </svg>
  <div class="fold" style="left:240px"></div>
  <div class="fold" style="left:480px"></div>

  <div class="block" style="left:18px;top:182px;width:206px">
    <h2 class="title-green">VMP-VITAL MATRIX <span>PROFILE</span></h2>
    <div class="rule rule--green"></div>
    <p class="body">Fernridge Wellness Co is changing the way people look at health by bringing the focus back to the physical examination and patient centered care. It's our new, cutting edge system, Vital Matrix Profile, that allows us to have unparalleled patient outcomes. Vital Matrix Profile is a true deep dive into the individual. The protocol assesses, measures and tracking over 70 different bio-parameters such as hormone balance, tissue health, muscle mass, fat mass, frame mass, water content, water distribution, and acid/alkaline balance. This new analytics tool allows hyper individualized and customized weight loss and health programs to evolve in a new and never before seen way.</p>
    <h2 class="title-green" style="margin-top:14px">LEANNESS &amp; <span>HEALTH</span></h2>
    <div class="rule rule--green"></div>
    <p class="body">The scientific community has held lean body composition as one of the 4 tenets in maintaining good health for decades. Yet, we are the fattest nation in the world. The weight loss industry is booming and failing all in the same. Lifestyle diseases are taking over our healthcare system with no definitive forms of treatment while at the same time, expensive drugs are failing our families, communities and nation. Why? The answer is lack of an effective way to assess, track and treat body composition. The scientific link between body composition and cellular health is the proof: the better your body, the better you look, and the better you can feel. If that's the case, then we are vain to want to look great! Fernridge Wellness Co is 100% OK with that. Whatever your reason for changing your body composition, weight loss, health or vanity, we're on board!</p>
  </div>

  <div class="block" style="left:258px;top:22px;width:206px">
    <h2 class="title-white">THE 4(16) <span>PLAN</span></h2>
    <div class="rule"></div>
    <p class="body on-dark">The 4(16) Cleanse plan works by creating a full metabolic reset geared towards facilitation of hormone optimization and balance as well as toxicity and fat removal. Toxins are fat soluble and often need targeted nutritional strategy for long-term weight loss to occur; this is why many people do not lose weight even on calorie restricted diets with exercise plans until they use proper nutritional protocol. The 4(16) Cleanse allows for fat cells to be released and disposed of while at the same time adding deficient nutrients back into the tissues, helping you to not only lose weight, but reach optimal health and hormonal balance at the same time.</p>
  </div>

  <div class="block" style="left:252px;top:440px;width:200px">
    <h3 class="tagline">Being Lean for Health<br>and Vanity ='s Healthy Vanity!</h3>
    <div class="rule rule--green"></div>
    <p class="body">Dr. Anton has coined the term "healthy vanity" to popularize the realization that looking and feeling good are often one in the same, that we shouldn't feel guilty for making and wanting our insides, and our outsides, to be healthy as well as aesthetically pleasing.</p>
  </div>

  <div class="block" style="left:498px;top:22px;width:206px">
    <h2 class="title-white">THE 4(16) <span>Cleanse</span></h2>
    <div class="rule"></div>
    <p class="body on-dark">The 4(16) Cleanse is an intensive detoxification week followed by a sixteen day reset plan. All 4(16) plans are completely customized. Our nutrition team guides every client through the intensive first week, then tailors each following phase to the results of their profile, so the gains made continue long after the plan is complete.</p>
    <h3 class="title-white" style="font-size:11px;margin-top:14px">Why We Chose Detox as our Primary Method of Treatment</h3>
    <div class="rule"></div>
    <p class="body on-dark">An interesting study was published in the 90s and it talked about the signs and symptoms of chronic toxicity. Nearly every complaint we see in practice, from fatigue and poor sleep to stubborn weight and headaches, appears on that list. Fernridge Wellness Co uses detoxification as a baseline for treatment. Conventional medicine tends to add and add medications to manage symptoms; we choose to remove the burden first. When toxins are cleared, the body has the room it needs to heal, restore balance and respond to every therapy that follows.</p>
    <h3 class="title-white" style="font-size:11px;margin-top:14px">Why The Emphasis on Removing Toxins</h3>
    <div class="rule"></div>
    <p class="body on-dark">There are over 80,000 registered chemicals in the environment, and for most of them, little is known about how they affect the human body. We are exposed through food, water, air and everyday products, and many of these compounds are stored in fat tissue for years. Science over the past 20 years has identified a large number of them as disruptors of hormones, metabolism and energy. They can slow weight loss, cloud the mind and strain the organs that keep us well. Removing them is the clearest path back to health, and the way our body produces and uses energy proves it to us with every client.</p>
  </div>
</section>

</body>
</html>
```